Homepage design competition to choose a designer for $1500 full website for a Small Animal Veterinar

We are running a homepage design competition to choose a designer who will later code an entire website. Please note, this competition is only for the front page design. There will be an additional payment of $1500 (Australian $AUD) for the complete website design including coding payment.

Front Page: First we need a front page design for our companion animal veterinary hospital. I will use the frontpage design competition to choose a designer for the full website.
Marlow Vet Clinic is a companion animal veterinary hospital in Ashby NSW. We provide veterinary medical and surgical treatment for dogs, cats, rabbits, birds and reptiles. Mostly dogs and cats.
Our reception is a 120 year old church and the hospital is 6 years old and custom built.
I want the site to be amazing. The sort of thing that could win prizes. The front page should be simple, fun and engaging whilst maintaining a strong sense of professionalism. Simple and elegant visual effects with subtle movement. The winning design will show originality.
Our main demographic is women aged 25 to 44 years old. We are a coal mining town. Most of our money comes from coal miners wives.
The front page must display our phone number and link to our facebook page. Otherwise the front page can have anything. The front page should impress new clients and reassure existing clients.
We pride ourselves on following up everything and caring for pets and their people their entire life. Please see our existing (horrible) website for more details about our business. http://www.marlowvetclinic.example/
Incorporate only amazing things from the old website. I hate the old website, so there is probably not much to use. We need something new and amazing.
Fully responsive design.

Characters: We have a logo and animal characters to incorporate into the design. These characters will be used throughout our email and facebook advertising. If they could be used with some movement and sound effects, that would be cool, but nothing too childish or silly.

Live site: please include links to live demo sites if possible.
Please include links to your other work.

Full Website: The successful designer of the frontpage must be able to demonstrate the ability produce a full website. The full website designer will be commissioned after the front page is chosen. We have budgeted for a full website of $1500.
I need to be able to add new articles to the website that will link from email newsletters and facebook, so the full website will need to be something I can modify or add to.
I have a working knowledge of Joomla, Wordpress and html.
The full website will have map, history of the hospital, history of the chapel, links to local services, pet care advice, memorials.
Ideally the winning designer will be able to integrate appointments available with our existing veterinary management software.
Fully responsive design.

Here are some websites that I like:
https://drbexley.example.au/
http://quincepepper.example/
http://www.xn--dorotawelnicka-abc12k.example/
https://www.zov.example.au/
https://www.frisko.example.au/
https://topmowers.example.au/
https://www.redgatecider.example/

Target Market(s)

Women aged 25 to 44 years

Industry/Entity Type

Veterinary

Number of Pages Required

1 page

Font styles to use
Serif
Sans Serif

Requirements
Must have
• Phone number
• social page Link https://www.facebook.com/marlow.vetclinic?v=wall
• Simplicity
• Originality
• Animal characters-images attached
Nice to have
• Images
• Clean
• Link to live site.
• Links to your other work.
• Demonstrate ability to integrate appointment booking with our veterinary software
Should not have
• Heaps of words
• Complexity

```html
<!DOCTYPE html>
<html lang="en">
<head>
<meta charset="utf-8">
<title>Marlow Vet Clinic</title>
<link href="https://fonts.googleapis.com/css2?family=Open+Sans:wght@400;600;700&family=Roboto+Condensed:wght@400;700&display=swap" rel="stylesheet">
<style>
:root{
  --green:#6e9a35;
  --green-dark:#5b8229;
  --ink:#3a3a3a;
  --text:#555;
  --muted:#777;
  --strip:#4b4b4b;
  --panel:#e6e6e6;
  --footer:#1d1d1d;
  --footer-bottom:#0b0b0b;
  --white:#fff;
}
*{box-sizing:border-box;margin:0;padding:0}
html,body{width:1200px;height:2913px;overflow:hidden}
body{font-family:"Open Sans",Arial,sans-serif;color:var(--text);background:var(--white);position:relative}
a{color:inherit;text-decoration:none}

/* top bar */
.topbar{position:absolute;left:0;top:0;width:1200px;height:28px;background:var(--green);color:var(--white);font-family:"Roboto Condensed",Arial,sans-serif;font-weight:700;font-size:14px}
.topbar .phones{position:absolute;left:161px;top:5px;display:flex;align-items:center;gap:8px}
.topbar .follow{position:absolute;right:161px;top:5px;display:flex;align-items:center;gap:8px;font-size:12px}
.round-icon{width:19px;height:19px;border:1.5px solid var(--white);border-radius:50%;display:inline-block}

/* nav */
.nav{position:absolute;top:28px;left:0;width:1200px;height:73px;background:var(--white)}
.brand{position:absolute;left:161px;top:18px;display:flex;align-items:center;gap:8px;font-family:"Roboto Condensed",Arial,sans-serif;font-weight:700;font-size:17px;color:var(--green-dark)}
.brand-dot{width:26px;height:26px;border-radius:50%;background:var(--green)}
.menu{position:absolute;right:161px;top:24px;display:flex;gap:26px;font-family:"Roboto Condensed",Arial,sans-serif;font-size:13px;color:var(--ink);text-transform:uppercase}
.menu .active{color:var(--green);position:relative}
.menu .active::after{content:"";position:absolute;left:50%;top:22px;width:7px;height:7px;margin-left:-3.5px;border-radius:50%;background:var(--green)}

/* hero */
.hero{position:absolute;top:101px;left:0;width:1200px;height:522px;background:linear-gradient(100deg,#3d4a2a 0%,#5d6b3c 30%,#8c8456 55%,#6a5a3d 75%,#3a3024 100%)}
.hero-copy{position:absolute;left:161px;top:170px;width:360px;color:var(--white)}
.hero-copy h1{font-family:"Roboto Condensed",Arial,sans-serif;font-weight:700;font-size:36px;line-height:1;margin-bottom:16px;letter-spacing:.5px}
.hero-copy h1 span{color:#86b447}
.hero-copy p{font-size:12.5px;line-height:19px}
.btn{display:inline-block;background:var(--green);color:var(--white);font-family:"Roboto Condensed",Arial,sans-serif;font-size:12px;text-transform:uppercase;padding:12px 16px}
.hero .btn{margin-top:26px;padding:13px 17px}
.slide-arrow{position:absolute;top:235px;width:44px;height:46px;border:1px solid rgba(255,255,255,.55);background:rgba(0,0,0,.15)}
.slide-arrow svg{position:absolute;left:16px;top:17px}

/* info strip */
.info{position:absolute;top:623px;left:0;width:1200px;height:154px;background:var(--strip);color:var(--white);font-family:"Roboto Condensed",Arial,sans-serif;font-weight:700;font-size:13px;text-transform:uppercase;text-align:center;line-height:28px}
.info-col{position:absolute;top:24px;width:260px}
.info-icon{width:40px;height:40px;border:2px solid var(--white);border-radius:50%;margin:0 auto 18px;display:flex;align-items:center;justify-content:center}

/* section titles */
.section-title{position:absolute;left:0;width:1200px;text-align:center;font-family:"Roboto Condensed",Arial,sans-serif;font-weight:700;font-size:27px;color:var(--ink);text-transform:uppercase}
.title-mark{position:absolute;left:555px;width:90px;height:14px}

/* services */
.services-intro{position:absolute;top:893px;left:400px;width:400px;text-align:center;font-size:12px;line-height:22px;color:var(--text)}
.service{position:absolute;width:238px;font-size:11px;line-height:15px;color:var(--text)}
.service h3{position:relative;font-family:"Roboto Condensed",Arial,sans-serif;font-weight:700;font-size:12px;color:var(--green);text-transform:uppercase;margin-bottom:10px;line-height:18px}
.service.left{left:171px;text-align:right}
.service.left h3{padding-right:38px}
.service.right{left:790px}
.service.right h3{padding-left:40px}
.service .icon{position:absolute;top:-3px;width:24px;height:24px}
.service.left .icon{right:4px}
.service.right .icon{left:10px}
.characters{position:absolute;left:452px;top:1018px;width:300px;height:320px;border-radius:8px;background:radial-gradient(ellipse at 40% 50%,#c7a98b 0%,#e8dccd 55%,#fff 80%)}

/* appointment */
.appt-photo{position:absolute;top:1503px;left:0;width:588px;height:357px;background:linear-gradient(120deg,#1f2118 0%,#2a2b22 45%,#3f5a24 80%,#6d8c3a 100%)}
.appt-panel{position:absolute;top:1503px;left:588px;width:612px;height:357px;background:var(--panel)}
.appt-panel p{position:absolute;left:24px;top:18px;width:428px;font-size:11px;line-height:14px;color:var(--muted)}
.field{position:absolute;width:202px;height:30px;background:var(--white);border:1px solid #d0d0d0;font-family:"Roboto Condensed",Arial,sans-serif;font-size:11px;color:#777;text-transform:uppercase;padding:8px 9px}
.field svg{position:absolute;right:9px;top:10px}
.textarea{height:64px;width:427px}
.appt-panel .btn{position:absolute;left:24px;top:305px;padding:9px 16px;font-size:12px}

/* testimonial */
.quote-badge{position:absolute;top:2008px;left:565px;width:70px;height:70px;border-radius:50%;background:var(--green);color:var(--white);font-family:Georgia,serif;font-size:46px;font-weight:700;text-align:center;line-height:84px}
.quote-text{position:absolute;top:2106px;left:300px;width:600px;text-align:center;font-size:15px;line-height:22px;color:#444}
.dots{position:absolute;top:2208px;left:572px;display:flex;gap:6px}
.dots span{width:11px;height:11px;background:var(--strip)}
.dots span.on{background:var(--green)}

/* map */
.map{position:absolute;top:2274px;left:0;width:1200px;height:293px;background:linear-gradient(180deg,#e9e9e9,#dcdcdc)}
.map-card{position:absolute;left:519px;top:72px;width:176px;height:64px;background:var(--white);box-shadow:0 1px 4px rgba(0,0,0,.25);font-size:11px;line-height:17px;color:#333;padding:12px}
.map-pin{position:absolute;left:598px;top:150px}

/* footer */
.footer{position:absolute;top:2567px;left:0;width:1200px;height:274px;background:var(--footer);color:#bbb;font-size:10px}
.footer h4{font-family:"Roboto Condensed",Arial,sans-serif;font-weight:700;font-size:13px;color:var(--white);text-transform:uppercase;margin-bottom:26px;position:relative}
.footer h4::after{content:"";position:absolute;left:0;top:20px;width:32px;height:2px;background:var(--green)}
.fcol{position:absolute;top:26px}
.fcol .brand-foot{display:flex;align-items:center;gap:8px;font-family:"Roboto Condensed",Arial,sans-serif;font-weight:700;font-size:16px;color:var(--white);margin-bottom:22px}
.fcol .brand-foot i{width:22px;height:22px;border-radius:50%;background:#777;display:block}
.fcol p{line-height:20px}
.contact-row{display:flex;align-items:flex-start;gap:14px;padding-bottom:14px;margin-bottom:14px;border-bottom:1px solid #444;width:186px;line-height:20px;white-space:nowrap}
.contact-row .ci{width:22px;height:22px;border-radius:50%;background:#555;flex:none;display:flex;align-items:center;justify-content:center}
.hours-row{width:186px;padding-bottom:20px;margin-bottom:22px;border-bottom:1px solid #444;white-space:nowrap}
.finput{width:204px;height:30px;border:1px solid #ddd;color:#ddd;padding:7px 6px;margin-top:12px}
.finput.tall{height:60px}
.footer .btn{margin-top:12px;padding:6px 14px;font-size:11px}
.bottom{position:absolute;top:2841px;left:0;width:1200px;height:72px;background:var(--footer-bottom);color:#aaa;font-size:10px;text-align:center;line-height:72px}
</style>
</head>
<body>

<header class="topbar">
  <div class="phones">
    <span class="round-icon"></span>
    <span>02 6500 1842 &nbsp;|&nbsp; 0491 570 226</span>
  </div>
  <div class="follow">
    <span>FOLLOW US ON:</span>
    <a class="round-icon" href="#" aria-label="Our social page"></a>
  </div>
</header>

<nav class="nav">
  <div class="brand"><span class="brand-dot"></span>Marlow Vet Clinic</div>
  <div class="menu">
    <a class="active">Home</a><a>Services</a><a>Staff</a><a>Contact</a><a>Map</a><a>History</a>
  </div>
</nav>

<section class="hero" role="img" aria-label="Photo of a small terrier sitting on a sunny grass lawn">
  <div class="slide-arrow" style="left:16px"><svg width="10" height="12" viewBox="0 0 10 12"><path d="M7 1 2 6l5 5" stroke="#fff" stroke-width="1.5" fill="none"/></svg></div>
  <div class="slide-arrow" style="right:16px"><svg width="10" height="12" viewBox="0 0 10 12"><path d="M3 1l5 5-5 5" stroke="#fff" stroke-width="1.5" fill="none"/></svg></div>
  <div class="hero-copy">
    <h1>WE KNOW <span>PET</span> HEALTH</h1>
    <p>Pellentesque commodo quis quam vel viverra. Donec luctus risus quis mauris rhoncus sollicitudin. Integer magna nulla, lacinia ac hendrerit sit amet, ultricies vel nisi.</p>
    <a class="btn">Learn More</a>
  </div>
</section>

<section class="info">
  <div class="info-col" style="left:170px">
    <div class="info-icon"><svg width="18" height="18" viewBox="0 0 24 24"><path d="M6.6 10.8a15 15 0 0 0 6.6 6.6l2.2-2.2c.3-.3.7-.4 1-.2 1.1.4 2.3.6 3.6.6.6 0 1 .4 1 1V20c0 .6-.4 1-1 1A17 17 0 0 1 3 4c0-.6.4-1 1-1h3.5c.6 0 1 .4 1 1 0 1.3.2 2.5.6 3.6.1.3 0 .7-.2 1z" fill="#fff"/></svg></div>
    Phone: 02 6500 1842<br>Emergency: 0491 570 226
  </div>
  <div class="info-col" style="left:470px">
    <div class="info-icon"><svg width="18" height="18" viewBox="0 0 24 24"><rect x="3" y="5" width="18" height="16" rx="2" fill="none" stroke="#fff" stroke-width="2"/><path d="M3 10h18M8 3v4M16 3v4" stroke="#fff" stroke-width="2"/></svg></div>
    Online Appointment<br>Book Now
  </div>
  <div class="info-col" style="left:770px">
    <div class="info-icon"><svg width="18" height="18" viewBox="0 0 24 24"><circle cx="12" cy="12" r="9" fill="none" stroke="#fff" stroke-width="2"/><path d="M12 7v5l3 2" stroke="#fff" stroke-width="2" fill="none"/></svg></div>
    Monday to Friday - 8:30am to 5:30pm<br>Saturday - 9:00am to 12:00 midday
  </div>
</section>

<h2 class="section-title" style="top:820px">Our Services</h2>
<svg class="title-mark" style="top:858px" viewBox="0 0 90 14"><path d="M0 7h32M58 7h32" stroke="#8db35a" stroke-width="1"/><g fill="#6e9a35"><ellipse cx="45" cy="9" rx="4" ry="3.3"/><circle cx="39.5" cy="5" r="1.6"/><circle cx="43" cy="2.5" r="1.6"/><circle cx="47" cy="2.5" r="1.6"/><circle cx="50.5" cy="5" r="1.6"/></g></svg>
<p class="services-intro">Phasellus at lacus non sem consequat accumsan quisque lorem libero, feugiat sit amet commodo et, venenatis ac justo.</p>

<div class="service left" style="top:996px"><h3>Vaccinations<svg class="icon" viewBox="0 0 24 24"><path d="M4 20l4-4M7 17l9-9 3 3-9 9zM15 5l4 4M18 2l4 4" stroke="#6e9a35" stroke-width="2" fill="none"/></svg></h3>Sed quis condimentum quam. Morbi condimenegestas quam, tempus ornare tortor vivamus ultricie</div>
<div class="service left" style="top:1091px"><h3>Emergency Surgery<svg class="icon" viewBox="0 0 24 24"><path d="M3 21 19 5l2 2L5 21z" fill="#6e9a35"/><path d="M2 22h8" stroke="#6e9a35" stroke-width="2"/></svg></h3>Sed quis condimentum quam. Morbi condimenegestas quam, tempus ornare tortor vivamus ultricie</div>
<div class="service left" style="top:1185px"><h3>Dental<svg class="icon" viewBox="0 0 24 24"><path d="M4 3h16l-5 18h-6z" fill="#6e9a35"/></svg></h3>Sed quis condimentum quam. Morbi condimenegestas quam, tempus ornare tortor vivamus ultricie</div>
<div class="service left" style="top:1291px"><h3>Radiology<svg class="icon" viewBox="0 0 24 24"><g fill="#6e9a35"><ellipse cx="12" cy="16" rx="6" ry="5"/><circle cx="4" cy="9" r="2.5"/><circle cx="9" cy="4.5" r="2.5"/><circle cx="15" cy="4.5" r="2.5"/><circle cx="20" cy="9" r="2.5"/></g></svg></h3>Sed quis condimentum quam. Morbi condimenegestas quam, tempus ornare tortor vivamus ultricie</div>

<div class="characters" role="img" aria-label="Illustration of the clinic's dog and cat characters sitting together"></div>

<div class="service right" style="top:996px"><h3>Ultrasound<svg class="icon" viewBox="0 0 24 24"><path d="M6 22l3-10 8-9 3 3-9 8z" fill="#6e9a35"/></svg></h3>Sed quis condimentum quam. Morbi condimenegestas quam, tempus ornare tortor vivamus ultricie</div>
<div class="service right" style="top:1091px"><h3>Routine Blood Tests<svg class="icon" viewBox="0 0 24 24"><rect x="6" y="6" width="12" height="16" rx="2" fill="#6e9a35"/><rect x="9" y="2" width="6" height="4" fill="#6e9a35"/></svg></h3>Sed quis condimentum quam. Morbi condimenegestas quam, tempus ornare tortor vivamus ultricie</div>
<div class="service right" style="top:1185px"><h3>Orthopaedic Surgery<svg class="icon" viewBox="0 0 24 24"><path d="M12 2v20M8 6l4-2 4 2M8 12h8" stroke="#6e9a35" stroke-width="2.5" fill="none"/></svg></h3>Sed quis condimentum quam. Morbi condimenegestas quam, tempus ornare tortor vivamus ultricie</div>
<div class="service right" style="top:1291px"><h3>Skin Treatments<svg class="icon" viewBox="0 0 24 24"><rect x="3" y="10" width="16" height="8" rx="3" fill="#6e9a35"/><path d="M5 18v3M17 18v3M19 11l3-3" stroke="#6e9a35" stroke-width="2"/></svg></h3>Sed quis condimentum quam. Morbi condimenegestas quam, tempus ornare tortor vivamus ultricie</div>

<h2 class="section-title" style="top:1414px">Make an Appointment</h2>
<svg class="title-mark" style="top:1452px" viewBox="0 0 90 14"><path d="M0 7h32M58 7h32" stroke="#8db35a" stroke-width="1"/><g fill="#6e9a35"><ellipse cx="45" cy="9" rx="4" ry="3.3"/><circle cx="39.5" cy="5" r="1.6"/><circle cx="43" cy="2.5" r="1.6"/><circle cx="47" cy="2.5" r="1.6"/><circle cx="50.5" cy="5" r="1.6"/></g></svg>

<div class="appt-photo" role="img" aria-label="Photo of a black labrador puppy lying in green grass"></div>
<form class="appt-panel">
  <p>Integer a justo vitae neque scelerisque tempus. Curabitur ante nulla, rutrum eu orci eu, tincidunt euismod urna. Integer nec erat vel justo sodales interdum. Morbi semper ante ut nulla ornare, non hendrerit elit consectetur.</p>
  <div class="field" style="left:24px;top:74px">Your Name</div>
  <div class="field" style="left:247px;top:74px">Pet Name</div>
  <div class="field" style="left:24px;top:123px">Phone</div>
  <div class="field" style="left:247px;top:123px">Select Pet Category<svg width="8" height="6" viewBox="0 0 8 6"><path d="M0 0h8L4 6z" fill="#777"/></svg></div>
  <div class="field" style="left:24px;top:173px">Date<svg width="10" height="10" viewBox="0 0 10 10"><rect x=".5" y="1.5" width="9" height="8" fill="none" stroke="#777"/><path d="M0 4h10" stroke="#777"/></svg></div>
  <div class="field" style="left:247px;top:173px">Preferred Time<svg width="8" height="6" viewBox="0 0 8 6"><path d="M0 0h8L4 6z" fill="#777"/></svg></div>
  <div class="field textarea" style="left:24px;top:219px"></div>
  <a class="btn">Book Now</a>
</form>

<h2 class="section-title" style="top:1911px">Client Speak</h2>
<svg class="title-mark" style="top:1949px" viewBox="0 0 90 14"><path d="M0 7h32M58 7h32" stroke="#8db35a" stroke-width="1"/><g fill="#6e9a35"><ellipse cx="45" cy="9" rx="4" ry="3.3"/><circle cx="39.5" cy="5" r="1.6"/><circle cx="43" cy="2.5" r="1.6"/><circle cx="47" cy="2.5" r="1.6"/><circle cx="50.5" cy="5" r="1.6"/></g></svg>
<div class="quote-badge">&ldquo;</div>
<p class="quote-text">Claritas est etiam processus dynamicus, qui sequitur mutationem consuetudium lectorum. Mirum est notare quam littera gothica, quam nunc putamus parum claram, anteposuerit litterarum.</p>
<div class="dots"><span class="on"></span><span></span><span></span><span></span></div>

<section class="map" role="img" aria-label="Street map of the neighbourhood showing the clinic location">
  <div class="map-card">14 Wren Cl Ashby Heights<br>NSW 2463</div>
  <svg class="map-pin" width="18" height="26" viewBox="0 0 18 26"><path d="M9 0a9 9 0 0 1 9 9c0 7-9 17-9 17S0 16 0 9a9 9 0 0 1 9-9z" fill="#d33"/><circle cx="9" cy="9" r="3" fill="#7a1010"/></svg>
</section>

<footer class="footer">
  <div class="fcol" style="left:161px;width:190px">
    <h4>About Us</h4>
    <div class="brand-foot"><i></i>Marlow Vet Clinic</div>
    <p>Marlow Vet Clinic is a Companion Animal Veterinary Hospital in Ashby committed to providing excellent care for loved pets and their owners.</p>
  </div>
  <div class="fcol" style="left:388px">
    <h4>Get in Touch</h4>
    <div class="contact-row"><span class="ci"><svg width="9" height="12" viewBox="0 0 9 12"><path d="M4.5 0A4.5 4.5 0 0 1 9 4.5C9 8 4.5 12 4.5 12S0 8 0 4.5A4.5 4.5 0 0 1 4.5 0z" fill="#ccc"/></svg></span><span>14 Wren Cl Ashby Heights<br>NSW 2463</span></div>
    <div class="contact-row"><span class="ci"><svg width="10" height="10" viewBox="0 0 24 24"><path d="M6.6 10.8a15 15 0 0 0 6.6 6.6l2.2-2.2c.3-.3.7-.4 1-.2 1.1.4 2.3.6 3.6.6.6 0 1 .4 1 1V20c0 .6-.4 1-1 1A17 17 0 0 1 3 4c0-.6.4-1 1-1h3.5c.6 0 1 .4 1 1 0 1.3.2 2.5.6 3.6.1.3 0 .7-.2 1z" fill="#ccc"/></svg></span><span>02 6500 1842 &nbsp;|&nbsp; 0491 570 226</span></div>
    <div class="contact-row"><span class="ci"><svg width="11" height="8" viewBox="0 0 11 8"><rect x=".5" y=".5" width="10" height="7" fill="none" stroke="#ccc"/><path d="M.5.5l5 4 5-4" stroke="#ccc" fill="none"/></svg></span><span>info@marlowvetclinic.example</span></div>
  </div>
  <div class="fcol" style="left:612px">
    <h4>Working Time</h4>
    <div class="hours-row">Monday to Friday - 8.30am to 5:30pm</div>
    <div class="hours-row">Saturday - 9:00am to 12:00 midday</div>
    <div class="hours-row">Sunday closed</div>
  </div>
  <div class="fcol" style="left:835px;width:204px">
    <h4>Qucik Contact</h4>
    <p>Lorem ipsum dolor sit amet, consectetur adipiscing elit.</p>
    <div class="finput">Type your email</div>
    <div class="finput tall">Message</div>
    <a class="btn">Send</a>
  </div>
</footer>
<div class="bottom">Copyright © 2017 marlowvetclinic.example. All rights reserved</div>

</body>
</html>
```